New Dynamic Design Based on Other Site

We need a new website designed where the front page is VERY SEO Friendly. The front page should almost follow the same SEO principles that are on RankLoomPress.com. The inner pages need to follow the same exact video animations that occur on brivox.com. I'd like to keep our "harrowicks" theme throughout the new design but we will provide all of the content but I want someone to design something SEO friendly, new blog theme, and actual inner pages that are dynamic and based on those short videos.

Check attached file for company name and site that we currently have. Feel free to pull the content from that site and re-use it and also leave placeholders for the rest of them.

PLEASE NO USE OF STOCK IMAGES. Use a designer or an illustrator to create the various images.
Updates

Please make sure the front page is SEO friendly! Make sure you familiarize yourself with the quorbit algorithm for SEO. Content above the fold H1 Tags Very mobile friendly Minimal javascript and animations Basically a quality static page with optimized content

Target Market(s)

call center companies, anything call related

Industry/Entity Type

Telecommunications

Number of Pages Required

4 page

Font styles to use
Sans Serif

Colors
33a6d7
85cae6
0792cd
0255a3
cee9f5
ecf7fb
ffffff

Requirements
Must have
• places for video animations
• dynamic functionality
• SEO friendly (front page)
Should not have
• should not look like a template. needs to be unique

```html
<!DOCTYPE html>
<html lang="en">
<head>
<meta charset="utf-8">
<title>DialMerit Blog</title>
<link rel="stylesheet" href="https://fonts.googleapis.com/css2?family=Lato:wght@400;700;900&family=Roboto:wght@400;500&display=swap">
<style>
:root{
  --sky:#33a6d7;
  --sky-soft:#85cae6;
  --azure:#0792cd;
  --navy:#0255a3;
  --ice:#cee9f5;
  --mist:#ecf7fb;
  --white:#ffffff;
  --ink:#1d1d1d;
  --ink-dark:#0d2a4a;
  --muted:#6b6b6b;
  --line:#dcdcdc;
  --hero:#bfe1e2;
  --footer:#0a55a8;
}
*{box-sizing:border-box;margin:0;padding:0}
html,body{width:1200px;height:2490px;overflow:hidden;background:var(--white)}
body{position:relative;font-family:"Lato",sans-serif;color:var(--ink)}
a{color:inherit;text-decoration:none}

/* header */
.site-header{position:absolute;left:0;top:0;width:1200px;height:133px;background:var(--white)}
.brand{position:absolute;left:125px;top:52px;display:flex;align-items:center;gap:10px}
.brand-dot{width:26px;height:26px;border-radius:50%;background:var(--azure)}
.brand-name{font-weight:700;font-size:30px;color:var(--navy);letter-spacing:-0.3px}
.call-now{position:absolute;left:718px;top:28px;display:flex;align-items:center;gap:10px}
.call-now svg{width:34px;height:34px}
.call-label{font-size:11px;font-weight:700;color:var(--ink-dark);letter-spacing:.3px;text-transform:uppercase;line-height:1.1}
.call-number{font-size:18px;font-weight:900;color:var(--azure);line-height:1.1}
.search{position:absolute;left:910px;top:25px;width:153px;height:37px;border:1px solid #cfcfcf;display:flex;align-items:center;gap:8px;padding-left:14px;font-size:9px;color:#888;letter-spacing:.5px}
.search svg{width:10px;height:10px}
.main-nav{position:absolute;top:92px;left:634px;font-size:11px;font-weight:700;color:var(--ink-dark);letter-spacing:.3px}
.main-nav a{position:absolute;white-space:nowrap}
.main-nav .is-current{color:var(--sky)}
.login-btn{position:absolute;left:984px;top:85px;width:78px;height:28px;background:var(--sky);color:var(--white);font-size:11px;font-weight:700;display:flex;align-items:center;justify-content:center;gap:6px;border-radius:2px}
.login-btn svg{width:9px;height:10px}

/* hero */
.hero{position:absolute;left:0;top:133px;width:1200px;height:412px;
  background:
    radial-gradient(ellipse 520px 150px at 600px 150px,rgba(255,255,255,.35),rgba(255,255,255,0) 70%),
    radial-gradient(ellipse 420px 90px at 600px 330px,rgba(60,70,90,.28),rgba(60,70,90,0) 75%),
    linear-gradient(180deg,#c6e6e7 0%,var(--hero) 60%,#b4d9da 100%)}

/* blog list */
.blog-title{position:absolute;top:601px;left:0;width:1200px;text-align:center;font-size:16px;font-weight:900;color:var(--ink-dark);letter-spacing:1px}
.blog-title::after{content:"";display:block;width:44px;height:2px;background:var(--sky);margin:16px auto 0}
.post-grid{position:absolute;left:131px;top:684px;display:grid;grid-template-columns:repeat(3,302px);grid-template-rows:repeat(3,408px);column-gap:17px;row-gap:26px}
.post-card{border:1px solid var(--line);padding:8px;background:var(--white);position:relative}
.post-media{height:224px;width:100%;position:relative;overflow:hidden}
.post-body{padding:0 14px}
.post-title{position:absolute;left:22px;top:249px;font-family:"Roboto",sans-serif;font-size:13.5px;font-weight:400;line-height:1.3;color:var(--ink);white-space:nowrap}
.post-title.single{top:258px}
.post-excerpt{position:absolute;left:22px;top:292px;font-family:"Roboto",sans-serif;font-size:10.5px;line-height:1.55;color:var(--muted);white-space:nowrap}
.read-more{position:absolute;left:22px;top:363px;background:var(--sky);color:var(--white);font-size:9px;font-weight:500;font-family:"Roboto",sans-serif;letter-spacing:.3px;padding:4px 7px;text-transform:uppercase}

.tone-desk{background:
  radial-gradient(circle at 30% 35%,#bfe6f3 0,rgba(191,230,243,0) 45%),
  radial-gradient(circle at 80% 80%,#4f9cc1 0,rgba(79,156,193,0) 55%),
  linear-gradient(135deg,#7fc4dd,#2a7fa9)}
.tone-screen{background:
  radial-gradient(circle at 35% 45%,#2d8fe0 0,rgba(45,143,224,0) 38%),
  radial-gradient(circle at 80% 70%,#d9b59a 0,rgba(217,181,154,0) 30%),
  linear-gradient(135deg,#eef1f4,#a9b8c8)}
.tone-agent{background:
  radial-gradient(circle at 50% 50%,#2d7fb8 0,#3b8cc2 36%,rgba(59,140,194,0) 48%),
  linear-gradient(135deg,#fde6d2,#f8d0ae)}
.tone-wood{background:
  radial-gradient(ellipse at 55% 50%,rgba(255,255,255,.12),rgba(255,255,255,0) 60%),
  linear-gradient(135deg,#7a4e2f,#3e2616)}
.tone-sketch{background:
  radial-gradient(circle at 25% 25%,rgba(233,95,45,.35),rgba(233,95,45,0) 35%),
  radial-gradient(circle at 70% 75%,rgba(233,95,45,.25),rgba(233,95,45,0) 35%),
  linear-gradient(135deg,#f4f2ee,#dedad3)}
.tone-wall{background:
  radial-gradient(ellipse at 60% 55%,rgba(30,140,205,.55),rgba(30,140,205,0) 45%),
  linear-gradient(180deg,#3a2e20 0%,#d9cca3 18%,#cdb98b 80%,#5a4a33 100%)}
.tone-glow{background:
  radial-gradient(circle at 45% 40%,#7fd8ff 0,#1f8fe0 18%,rgba(15,77,152,0) 48%),
  linear-gradient(135deg,#0f4d98,#061b3f)}
.tone-tiles{background:
  radial-gradient(ellipse at 50% 45%,#d9ccb0 0,rgba(217,204,176,0) 45%),
  linear-gradient(180deg,#8a6d47,#3a2918)}
.media-caption{position:absolute;left:6px;top:132px;width:234px;background:rgba(13,95,150,.9);color:var(--white);font-size:13px;line-height:1.4;padding:7px 9px;letter-spacing:.4px;text-transform:uppercase;font-family:"Roboto",sans-serif}
.media-caption strong{font-weight:500}

.more-btn{position:absolute;left:530px;top:2012px;width:141px;height:36px;background:var(--ink-dark);color:var(--white);font-size:10px;font-weight:700;letter-spacing:.4px;display:flex;align-items:center;justify-content:center;text-transform:uppercase}

/* footer */
.site-footer{position:absolute;left:0;top:2113px;width:1200px;height:377px;background:var(--footer);color:var(--white)}
.footer-heading{position:absolute;top:59px;font-size:11px;font-weight:900;letter-spacing:.4px;text-transform:uppercase}
.footer-list{position:absolute;top:88px;list-style:none;font-size:10px;font-variant:small-caps;line-height:16px;letter-spacing:.3px}
.footer-contact{position:absolute;left:307px;top:88px;font-size:10px;font-variant:small-caps;line-height:16px;letter-spacing:.3px}
.footer-contact p{margin-bottom:17px}
.email-field{position:absolute;left:551px;top:97px;width:236px;height:38px;background:var(--white);color:#777;font-size:10px;display:flex;align-items:center;padding-left:14px;letter-spacing:.5px}
.signup-btn{position:absolute;left:551px;top:148px;width:96px;height:30px;background:var(--sky);color:var(--white);font-size:11px;font-weight:900;letter-spacing:.5px;display:flex;align-items:center;justify-content:center}
.footer-brand{position:absolute;left:910px;top:92px;display:flex;align-items:center;gap:10px}
.footer-brand .brand-dot{background:var(--white)}
.footer-brand .brand-name{color:var(--white)}
.footer-rule{position:absolute;left:133px;top:256px;width:939px;height:1px;background:rgba(255,255,255,.2)}
.follow{position:absolute;left:133px;top:306px;display:flex;align-items:center;gap:10px;font-size:10px;font-weight:900;letter-spacing:.4px}
.social{display:flex;gap:13px;margin-left:14px}
.social span{width:27px;height:27px;border-radius:50%;background:var(--sky)}
.social span.warm{background:#e2573c}
.social span.slate{background:#3f6f86}
.social span.deep{background:#1777b8}
.copyright{position:absolute;right:128px;top:315px;font-size:9.5px;letter-spacing:.3px}
</style>
</head>
<body>

<header class="site-header">
  <a class="brand" href="#"><span class="brand-dot"></span><span class="brand-name">DialMerit</span></a>
  <div class="call-now">
    <svg viewBox="0 0 34 34" aria-hidden="true"><circle cx="17" cy="17" r="17" fill="#0792cd"/><path d="M12.5 9.5l3 3-1.8 2.2c.9 2 2.6 3.7 4.6 4.6l2.2-1.8 3 3-2 2.2c-5.6-.6-10.6-5.6-11.2-11.2z" fill="#fff"/></svg>
    <div><div class="call-label">Call us now</div><div class="call-number">855.410.2270</div></div>
  </div>
  <div class="search">
    <svg viewBox="0 0 10 10" aria-hidden="true"><circle cx="4" cy="4" r="3" fill="none" stroke="#555" stroke-width="1.2"/><path d="M6.3 6.3L9 9" stroke="#555" stroke-width="1.2"/></svg>
    SEARCH
  </div>
  <nav class="main-nav">
    <a href="#" style="left:0">WHO WE ARE</a>
    <a href="#" style="left:110px">SERVICES</a>
    <a href="#" class="is-current" style="left:198px">BLOG</a>
    <a href="#" style="left:268px">CONTACT</a>
  </nav>
  <a class="login-btn" href="#"><svg viewBox="0 0 9 10" aria-hidden="true"><rect x="0.5" y="4.5" width="8" height="5" fill="#fff"/><path d="M2 4.5V3a2.5 2.5 0 015 0v1.5" fill="none" stroke="#fff" stroke-width="1.2"/></svg>LOGIN</a>
</header>

<section class="hero" role="img" aria-label="Illustration of four call center agents with headsets working at laptops along a desk, beneath hanging lamps and floating colourful communication icons"></section>

<main>
  <h1 class="blog-title">BLOG</h1>
  <div class="post-grid">
    <article class="post-card">
      <div class="post-media tone-desk" role="img" aria-label="Photo of a desk with a monitor, keyboard and green mug">
        <div class="media-caption">The shift from<br><strong>“Voice” interactions,<br>to “Text”</strong></div>
      </div>
      <h2 class="post-title">The Text Revolution: A New<br>Era of Customer Service</h2>
      <p class="post-excerpt">Over the past decade, email, social media and<br>instant messaging technologies have ushered in<br>a new method of communication.</p>
      <a class="read-more" href="#">Read more</a>
    </article>
    <article class="post-card">
      <div class="post-media tone-screen" role="img" aria-label="Photo of a hand touching a screen of blue contact icons"></div>
      <h2 class="post-title">Speak up and Listen Closely: Effective<br>Communication in your Contact Center</h2>
      <p class="post-excerpt">Over the past decade, email, social media and<br>instant messaging technologies have ushered in<br>a new method of communication.</p>
      <a class="read-more" href="#">Read more</a>
    </article>
    <article class="post-card">
      <div class="post-media tone-agent" role="img" aria-label="Illustration of a headset agent with a globe, handshake and star"></div>
      <h2 class="post-title">A Guide on How to Hire Contact<br>Center Employees</h2>
      <p class="post-excerpt">Over the past decade, email, social media and<br>instant messaging technologies have ushered in<br>a new method of communication.</p>
      <a class="read-more" href="#">Read more</a>
    </article>
    <article class="post-card">
      <div class="post-media tone-wood" role="img" aria-label="Lettering on dark wood: motivating and rewarding exceptional agent performance"></div>
      <h2 class="post-title">The Keys to a Happier, More<br>Productive Contact Center</h2>
      <p class="post-excerpt">Over the past decade, email, social media and<br>instant messaging technologies have ushered in<br>a new method of communication.</p>
      <a class="read-more" href="#">Read more</a>
    </article>
    <article class="post-card">
      <div class="post-media tone-sketch" role="img" aria-label="Sketch of soft skills words such as empathy, trustworthiness and assertiveness"></div>
      <h2 class="post-title single">When Being “Soft” is a Good Thing</h2>
      <p class="post-excerpt">Over the past decade, email, social media and<br>instant messaging technologies have ushered in<br>a new method of communication.</p>
      <a class="read-more" href="#">Read more</a>
    </article>
    <article class="post-card">
      <div class="post-media tone-wall" role="img" aria-label="Blue script lettering painted on a weathered wall"></div>
      <h2 class="post-title">Back to the Basics: Quality<br>Monitoring Essentials</h2>
      <p class="post-excerpt">Over the past decade, email, social media and<br>instant messaging technologies have ushered in<br>a new method of communication.</p>
      <a class="read-more" href="#">Read more</a>
    </article>
    <article class="post-card">
      <div class="post-media tone-glow" role="img" aria-label="Photo of a glowing digital globe above an open hand"></div>
      <h2 class="post-title">Contact Centers of the<br>21st Century</h2>
      <p class="post-excerpt">Over the past decade, email, social media and<br>instant messaging technologies have ushered in<br>a new method of communication.</p>
      <a class="read-more" href="#">Read more</a>
    </article>
    <article class="post-card">
      <div class="post-media tone-tiles" role="img" aria-label="Photo of wooden letter tiles spelling a word"></div>
      <h2 class="post-title">Building Better Trust Throughout<br>the QA Hierarchy</h2>
      <p class="post-excerpt">Over the past decade, email, social media and<br>instant messaging technologies have ushered in<br>a new method of communication.</p>
      <a class="read-more" href="#">Read more</a>
    </article>
    <article class="post-card">
      <div class="post-media tone-agent" role="img" aria-label="Illustration of a headset agent with a globe, handshake and star"></div>
      <h2 class="post-title">A Guide on How to Hire Contact<br>Center Employees</h2>
      <p class="post-excerpt">Over the past decade, email, social media and<br>instant messaging technologies have ushered in<br>a new method of communication.</p>
      <a class="read-more" href="#">Read more</a>
    </article>
  </div>
  <a class="more-btn" href="#">View more blogs</a>
</main>

<footer class="site-footer">
  <h3 class="footer-heading" style="left:133px">Menu</h3>
  <ul class="footer-list" style="left:133px">
    <li>Home</li><li>Who We Are</li><li>Services</li><li>Blog</li><li>Login</li>
  </ul>
  <h3 class="footer-heading" style="left:307px">Contact us</h3>
  <div class="footer-contact">
    <p>4820 Harbor Crest Ave<br>Linwood, CA 90412</p>
    <p>hello@dialmerit.com</p>
    <p>855.410.2270</p>
  </div>
  <h3 class="footer-heading" style="left:549px">Newsletter</h3>
  <div class="email-field">E MAIL ID</div>
  <a class="signup-btn" href="#">SIGNUP</a>
  <div class="footer-brand"><span class="brand-dot"></span><span class="brand-name">DialMerit</span></div>
  <div class="footer-rule"></div>
  <div class="follow">FOLLOW US
    <div class="social"><span class="deep"></span><span></span><span class="slate"></span><span class="warm"></span><span class="deep"></span></div>
  </div>
  <p class="copyright">© 2017 DIALMERIT. ALL RIGHTS RESERVED.</p>
</footer>

</body>
</html>
```